Bright Sprouts Newcastle Event Flyer

This flyer is to advertise a gathering of experts who each be speaking on different aspects of child health and development called on Bright Sprouts Newcastle.

Can it please include the logo attached.

Details in include:

July 25th 2015
12-4pm

Industry/Entity Type

Health

```html
<!DOCTYPE html>
<html lang="en">
<head>
<meta charset="utf-8">
<title>Bright Sprouts Newcastle – Child Health and Development Flyer</title>
<link href="https://fonts.googleapis.com/css2?family=Ubuntu:wght@400;500;700&display=swap" rel="stylesheet">
<style>
  :root {
    --canvas-bg: #e4e4e4;
    --paper: #ffffff;
    --leaf-light: #f4f9e8;
    --leaf-mid: #e2f0c2;
    --leaf-green: #b9dc6a;
    --panel-dark: #3c3c3c;
    --panel-stripe: #5b5b5b;
    --frame-dark: #2a2a2a;
    --orange: #f6a623;
    --brand-orange: #f07a2e;
    --call-box: #1c1c1c;
    --white: #ffffff;
    --footer-blue: #4a9fe0;
    --event-grey: #555555;
  }
  * { margin: 0; padding: 0; box-sizing: border-box; }
  html, body {
    width: 1200px;
    height: 800px;
    overflow: hidden;
    background: var(--canvas-bg);
    font-family: "Ubuntu", "Trebuchet MS", sans-serif;
  }
  .flyer {
    position: absolute;
    left: 338px;
    top: 30px;
    width: 524px;
    height: 740px;
    background: var(--paper);
    overflow: hidden;
    box-shadow: 0 6px 18px rgba(0,0,0,0.18);
  }
  .flyer__shapes {
    position: absolute;
    inset: 0;
  }
  .brand {
    position: absolute;
    left: 30px;
    top: 42px;
    display: flex;
    align-items: center;
    gap: 10px;
  }
  .brand__dot {
    width: 30px;
    height: 30px;
    border-radius: 50%;
    background: var(--brand-orange);
  }
  .brand__name {
    font-weight: 500;
    font-size: 22px;
    color: var(--brand-orange);
  }
  .quote-badge {
    position: absolute;
    left: 22px;
    top: 150px;
    width: 220px;
    height: 220px;
    border-radius: 50%;
    background: var(--orange);
    display: flex;
    align-items: center;
    justify-content: center;
    text-align: center;
    padding: 0 24px;
    box-shadow: 0 3px 8px rgba(0,0,0,0.15);
  }
  .quote-badge__text {
    color: var(--white);
    font-size: 13px;
    line-height: 1.45;
  }
  .quote-badge__author {
    display: block;
    font-weight: 500;
  }
  .event-title {
    position: absolute;
    left: 30px;
    top: 446px;
    color: var(--white);
    font-weight: 700;
    font-size: 40px;
    line-height: 1.15;
    letter-spacing: 0.5px;
  }
  .call-box {
    position: absolute;
    left: 322px;
    top: 410px;
    width: 186px;
    height: 70px;
    background: var(--call-box);
    border-radius: 8px;
    text-align: center;
    padding-top: 8px;
    box-shadow: 0 3px 6px rgba(0,0,0,0.35);
  }
  .call-box__label {
    display: block;
    color: var(--orange);
    font-weight: 700;
    font-size: 16px;
    letter-spacing: 1px;
  }
  .call-box__number {
    display: block;
    color: var(--white);
    font-weight: 500;
    font-size: 26px;
    letter-spacing: 0.5px;
  }
  .call-note {
    position: absolute;
    left: 330px;
    top: 494px;
    width: 178px;
    color: var(--orange);
    font-size: 11px;
    line-height: 1.45;
  }
  .footer {
    position: absolute;
    left: 0;
    bottom: 0;
    width: 100%;
    height: 88px;
    background: var(--paper);
    text-align: right;
    padding: 14px 34px 0 0;
    color: var(--footer-blue);
    font-size: 13px;
    line-height: 1.6;
  }
  .footer__event {
    display: block;
    color: var(--event-grey);
    font-weight: 500;
  }
</style>
</head>
<body>
  <article class="flyer">
    <svg class="flyer__shapes" width="524" height="740" viewBox="0 0 524 740" xmlns="http://www.w3.org/2000/svg">
      <defs>
        <linearGradient id="leafBackdrop" x1="0" y1="1" x2="1" y2="0">
          <stop offset="0" stop-color="#f4f9e8"/>
          <stop offset="0.55" stop-color="#e2f0c2"/>
          <stop offset="1" stop-color="#b9dc6a"/>
        </linearGradient>
        <linearGradient id="photoTones" x1="0" y1="0" x2="1" y2="1">
          <stop offset="0" stop-color="#f3e4d6"/>
          <stop offset="0.5" stop-color="#e7b9b3"/>
          <stop offset="1" stop-color="#c9d8e6"/>
        </linearGradient>
      </defs>
      <rect class="backdrop" x="0" y="0" width="524" height="652" fill="url(#leafBackdrop)" role="img" aria-label="Soft green leaf texture background"/>
      <polygon class="panel-stripe" points="0,414 524,336 524,352 0,430" fill="#5b5b5b"/>
      <polygon class="panel-dark" points="0,430 524,352 524,652 0,652" fill="#3c3c3c"/>
      <polygon class="photo-frame" points="176,96 524,96 524,372 218,372 176,330" fill="#2a2a2a"/>
      <polygon class="photo" points="192,112 524,112 524,356 224,356 192,324" fill="url(#photoTones)" role="img" aria-label="Photo of a smiling mother holding her baby while a practitioner examines the child"/>
    </svg>

    <div class="brand">
      <span class="brand__dot"></span>
      <span class="brand__name">Bright Sprouts</span>
    </div>

    <div class="quote-badge">
      <p class="quote-badge__text">
        "Children are our future, and my passion is to help them function as well as they can – to be as healthy and happy as possible"
        <span class="quote-badge__author">- Helen Marsh -</span>
      </p>
    </div>

    <h1 class="event-title">Child<br>Health<br>and<br>Development</h1>

    <div class="call-box">
      <span class="call-box__label">CALL :</span>
      <span class="call-box__number">02 4900 1234</span>
    </div>

    <p class="call-note">If you have a desire to learn more so that you can help the children in your practice</p>

    <footer class="footer">
      <span class="footer__event">Bright Sprouts Newcastle · July 25th 2015 · 12–4pm</span>
      Bright Sprouts Seminars | Kotara, New South Wales<br>
      www.brightsprouts.com.au
    </footer>
  </article>
</body>
</html>
```